Corliss Homes Website for luxury custom home builder with endless detail

Modern website for luxury custom home builder. Simple and easy for viewers to understand what we do. New company formed by retired custom home builder. Company concept is to simplify the building experience with modern technology and introduce a simple pricing strategy for the client. Website must flow. Prefer page less design or possibly something that is up and coming within the web design community. Two galleries: INTERIOR and EXTERIOR. I would like two click on box's when the website is opened showing the galleries as a centerpiece and would also prefer them to play as a slide show. The page needs to fit the entire screen in size. We would like to use Grey, Black and White or the shade of blue that is in our company logo. I would like to see one of my uploaded photos to be in the background. I would also like a 3rd box that will play some type of animated video describing what we do and what our process is. Hoping this would be more interactive for the viewer than clicking on buttons and navigating around wasting time.

Target Market(s)

affluent buyers ages 30-60 who want to built anything from large estates to downsized luzury homes for the retired crowd.

Industry/Entity Type

Home Builder

Number of Pages Required

1 page

Font styles to use
Sans Serif

Colors
33a6d7
000000
333333
5c5c5c
9d9d9d
d9d9d9

Requirements
Must have
• Logo and name at top of page. I would like a pageless web design that includes two gallery box's (Interior and Exterior photos) side by side on the first page. I would also like a 3rd box that will be a eVideo explaining what we do and how we do it. I want as little text as possible. I would like the background to be of one of my interior photos that will flow best and pop when the page loads.

```html
<!DOCTYPE html>
<html lang="en">
<head>
<meta charset="utf-8">
<title>Corliss Homes — Luxury custom home builder</title>
<link href="https://fonts.googleapis.com/css2?family=Gelasio:wght@400;700&display=swap" rel="stylesheet">
<style>
  :root {
    --blue: #33a6d7;
    --blue-light: #7fcbea;
    --black: #000000;
    --charcoal: #333333;
    --slate: #5c5c5c;
    --stone: #9d9d9d;
    --mist: #d9d9d9;
    --white: #ffffff;
    --ceiling: #4a2a1c;
    --wall: #b0704a;
    --wall-glow: #d99a6a;
    --floor: #a98a98;
    --floor-shade: #7a6070;
  }
  * { margin: 0; padding: 0; box-sizing: border-box; }
  html, body { width: 1200px; height: 632px; overflow: hidden; }
  body { font-family: "Gelasio", Georgia, serif; position: relative; background: var(--black); }

  .hero-photo {
    position: absolute; inset: 0;
    background:
      radial-gradient(ellipse 420px 180px at 880px 250px, rgba(235,170,110,0.55), rgba(235,170,110,0) 100%),
      radial-gradient(ellipse 300px 200px at 180px 230px, rgba(220,190,160,0.45), rgba(220,190,160,0) 100%),
      radial-gradient(ellipse 700px 160px at 620px 500px, rgba(200,175,190,0.55), rgba(200,175,190,0) 100%),
      linear-gradient(90deg, rgba(60,35,25,0.35) 0%, rgba(60,35,25,0) 12%, rgba(60,35,25,0) 88%, rgba(60,35,25,0.35) 100%),
      linear-gradient(180deg, var(--ceiling) 14%, #7a4630 24%, var(--wall) 38%, var(--wall-glow) 52%, #a88078 64%, var(--floor) 76%, var(--floor-shade) 100%);
  }

  .site-header {
    position: absolute; top: 0; left: 0; width: 1200px; height: 97px;
    background: rgba(255,255,255,0.95);
    box-shadow: 0 1px 3px rgba(0,0,0,0.15);
  }
  .brand { position: absolute; left: 150px; top: 16px; width: 146px; text-align: center; }
  .brand-square { display: block; margin: 0 auto; width: 46px; height: 46px; border: 2px solid var(--stone); }
  .brand-name {
    display: block; margin-top: 4px; color: var(--blue);
    font-size: 17px; line-height: 18px; font-variant: small-caps; white-space: nowrap;
  }

  .main-nav { position: absolute; left: 717px; top: 0; display: flex; }
  .main-nav a {
    display: block; height: 95px; padding: 66px 0 0; margin-right: 18px;
    color: var(--slate); font-size: 13px; text-decoration: none;
  }
  .main-nav a.is-active {
    background: var(--blue); color: var(--white); width: 55px; text-align: center;
    margin-right: 8px; border-bottom: 3px solid var(--blue-light);
  }

  .social { position: absolute; left: 947px; top: 21px; display: flex; gap: 2px; }
  .social span { width: 24px; height: 24px; border-radius: 50%; background: var(--stone); display: block; }

  .headline { position: absolute; left: 151px; top: 252px; color: var(--white); text-shadow: 0 1px 3px rgba(0,0,0,0.55); }
  .headline h1 { font-weight: 400; font-size: 38px; line-height: 46px; letter-spacing: 0.3px; }
  .headline p { margin: -7px 0 0 115px; font-size: 14px; }

  .preview {
    position: absolute; left: 150px; top: 457px; width: 215px; height: 102px;
    border: 3px solid var(--white);
  }
  .preview-photo { width: 100%; height: 100%; background: linear-gradient(180deg, #d6d6d6 0%, #bdb2a6 45%, #8a6a50 75%, #4a2c1c 100%); }
  .preview-pointer { position: absolute; left: 99px; bottom: -11px; }

  .gallery-bar { position: absolute; left: 0; top: 577px; width: 1200px; height: 55px; background: rgba(0,0,0,0.93); }
  .gallery-card { position: absolute; top: 0; height: 55px; padding: 6px 0 0; color: var(--slate); }
  .gallery-card h2 { font-size: 18px; font-weight: 700; color: var(--white); line-height: 20px; }
  .gallery-card p { font-size: 9px; line-height: 11px; margin-top: 3px; }
  .gallery-card.is-open { left: 150px; width: 215px; background: var(--white); padding-left: 8px; color: var(--slate); }
  .gallery-card.is-open h2 { color: var(--blue); }
  .gallery-card.exterior { left: 502px; }
  .gallery-card.video { left: 842px; }
  .divider { position: absolute; top: 0; width: 1px; height: 55px; background: #1e1e1e; }
  .slide-arrows { position: absolute; right: 10px; bottom: 7px; display: flex; gap: 2px; }
  .slide-arrows span { width: 14px; height: 11px; background: var(--stone); display: flex; align-items: center; justify-content: center; }
</style>
</head>
<body>
  <div class="hero-photo" role="img" aria-label="Covered patio of a luxury home with wicker chairs, dining set, stone arch and arched windows"></div>

  <header class="site-header">
    <div class="brand">
      <span class="brand-square"></span>
      <span class="brand-name">Corliss Homes</span>
    </div>
    <nav class="main-nav">
      <a href="#" class="is-active">About</a>
      <a href="#">Work</a>
      <a href="#">Latest</a>
      <a href="#">Explore</a>
      <a href="#">Awards</a>
      <a href="#">Contact</a>
    </nav>
    <div class="social" aria-label="Social links">
      <span></span><span></span><span></span><span></span>
    </div>
  </header>

  <div class="headline">
    <h1>Luxury custom home builder.</h1>
    <p>New company formed by retired custom home builder</p>
  </div>

  <div class="preview">
    <div class="preview-photo" role="img" aria-label="Interior dining room with long table and pendant light"></div>
    <svg class="preview-pointer" width="14" height="9" viewBox="0 0 14 9"><polygon points="0,0 14,0 7,8" fill="#ffffff"/></svg>
  </div>

  <section class="gallery-bar">
    <div class="divider" style="left:428px"></div>
    <div class="divider" style="left:743px"></div>
    <div class="divider" style="left:1061px"></div>

    <article class="gallery-card is-open">
      <h2>INTERIOR</h2>
      <p>Neque porro quisquam est qui<br>dolorem ipsum quia dolor sit amet,</p>
      <div class="slide-arrows">
        <span><svg width="8" height="5" viewBox="0 0 8 5"><path d="M8 2.5H1M3 0.5L1 2.5L3 4.5" stroke="#fff" fill="none"/></svg></span>
        <span><svg width="8" height="5" viewBox="0 0 8 5"><path d="M0 2.5H7M5 0.5L7 2.5L5 4.5" stroke="#fff" fill="none"/></svg></span>
      </div>
    </article>
    <article class="gallery-card exterior">
      <h2>EXTERIOR</h2>
      <p>Neque porro quisquam est qui<br>dolorem ipsum quia dolor sit amet,</p>
    </article>
    <article class="gallery-card video">
      <h2>OUR VIDEO</h2>
      <p>Neque porro quisquam est qui<br>dolorem ipsum quia dolor sit amet,</p>
    </article>
  </section>
</body>
</html>
```